Runlark

I have a web site RUNLARK.com that is in serious need of a re-design. The site is mean't to be a portal for an app that I have called RUNLARK which you can see in the app store or googleplay. Take a look and see what you can do.
Updates

Project Deadline Extended
Reason: Still working with designers. The "look" is not quite there but a lot of progress has been made. MB

Industry/Entity Type

Store

```html
<!DOCTYPE html>
<html lang="en">
<head>
<meta charset="utf-8">
<title>Runlark</title>
<link href="https://fonts.googleapis.com/css2?family=Open+Sans:wght@400;600;700;800&display=swap" rel="stylesheet">
<style>
:root{
  --page:#ececec;
  --column:#ffffff;
  --brand:#1d4596;
  --green:#2f9a3a;
  --green-dark:#1f7a2a;
  --panel:#2b2b2b;
  --panel-text:#e6e6e6;
  --ink:#1b1b1b;
  --muted:#555555;
  --free:#2a8fd6;
  --footer:#262626;
}
*{box-sizing:border-box;margin:0;padding:0}
html,body{width:1200px;height:2220px;overflow:hidden}
body{background:var(--page);font-family:"Open Sans",Arial,sans-serif;color:var(--ink);position:relative}
.column{position:absolute;left:192px;top:0;width:816px;height:2100px;background:var(--column)}
.logo{position:absolute;left:240px;top:30px;display:flex;align-items:center;gap:14px}
.logo-dot{width:40px;height:40px;border-radius:50%;background:var(--brand)}
.logo-name{font-size:62px;font-weight:800;color:var(--brand);letter-spacing:-1px;line-height:1}
.top-actions{position:absolute;left:808px;top:82px;display:flex;gap:12px}
.btn{height:40px;padding:0 18px;display:flex;align-items:center;font-size:17px;color:#fff}
.btn-search{background:var(--green)}
.btn-faq{background:#111;width:74px;justify-content:center}
.tagline{position:absolute;left:192px;width:816px;top:212px;text-align:center;font-size:23px;font-weight:700}
.slider{position:absolute;left:192px;top:264px;width:816px;height:288px;background:linear-gradient(135deg,#c9ccd3 0%,#7e6656 45%,#3a2a24 70%,#9aa0aa 100%)}
.slide-arrow{position:absolute;top:126px;width:34px;height:34px}
.slide-arrow.prev{left:18px}
.slide-arrow.next{right:18px}
.slide-dots{position:absolute;left:0;right:0;bottom:14px;display:flex;justify-content:center;gap:10px}
.slide-dots span{width:12px;height:12px;border-radius:50%;background:rgba(255,255,255,.55)}
.slide-dots span.on{background:#fff}
.banner{position:absolute;left:192px;top:592px;width:816px;height:88px;background:linear-gradient(180deg,var(--green) 0%,var(--green-dark) 100%);display:flex;align-items:center;justify-content:center;color:#fff;font-size:30px;font-weight:700}
.info{position:absolute;left:192px;top:680px;width:816px;height:456px;background:var(--panel);color:var(--panel-text);padding:36px 76px 0 108px;font-size:14px;line-height:1.45}
.info h3{font-size:14px;font-weight:700;color:#fff;margin-bottom:6px;white-space:nowrap}
.info ul{list-style:none;margin:0 0 20px 30px}
.info p{margin:0 0 20px 30px}
.info p:last-child{margin-bottom:0}
.phone{position:absolute;left:500px;top:1200px;width:200px;height:360px;border-radius:26px;background:#1a1a1a;padding:40px 14px}
.phone-screen{width:100%;height:100%;background:linear-gradient(180deg,#3e6fbf 0%,#e9eefa 30%,#ffffff 100%)}
.store-badge{position:absolute;left:530px;top:1582px;width:140px;height:50px;background:#000;border-radius:8px;border:2px solid #888}
.features{position:absolute;left:232px;top:1686px;width:740px;display:flex;justify-content:space-between}
.feature{width:220px}
.feature-shot{width:150px;height:134px;margin:0 auto 66px}
.shot-a{background:linear-gradient(135deg,#3c5b7a,#a2b6c8)}
.shot-b{background:linear-gradient(180deg,#1d3a2a,#4d8a5a 60%,#1a2a3a)}
.shot-c{background:linear-gradient(135deg,#c7dced,#6a95c2);border:3px solid #9bc0e0}
.feature h4{font-size:12px;font-weight:700;line-height:1.35;margin-bottom:8px}
.feature p{font-size:10px;color:var(--muted);line-height:1.4;margin-bottom:6px}
.free{font-size:26px;font-weight:800;color:var(--free);line-height:1}
.footer{position:absolute;left:0;top:2100px;width:1200px;height:120px;background:var(--footer)}
</style>
</head>
<body>
<div class="column"></div>

<header>
  <div class="logo"><span class="logo-dot"></span><span class="logo-name">Runlark</span></div>
  <nav class="top-actions">
    <span class="btn btn-search">Search</span>
    <span class="btn btn-faq">FAQ</span>
  </nav>
</header>

<h2 class="tagline">The sport statistics and information you want when you want them</h2>

<section class="slider" role="img" aria-label="Photo of a smiling basketball player holding a championship trophy">
  <svg class="slide-arrow prev" viewBox="0 0 34 34"><circle cx="17" cy="17" r="16" fill="rgba(0,0,0,.35)" stroke="#fff" stroke-width="1.5"/><path d="M20 10 L13 17 L20 24" fill="none" stroke="#fff" stroke-width="2.5"/></svg>
  <svg class="slide-arrow next" viewBox="0 0 34 34"><circle cx="17" cy="17" r="16" fill="rgba(0,0,0,.35)" stroke="#fff" stroke-width="1.5"/><path d="M14 10 L21 17 L14 24" fill="none" stroke="#fff" stroke-width="2.5"/></svg>
  <div class="slide-dots"><span class="on"></span><span></span><span></span></div>
</section>

<div class="banner">Watching a sporting event and need information?</div>

<section class="info">
  <h3>RUNLARK PROVIDES IMMEDIATE ACCESS TO THE INFORMATION YOU NEED:</h3>
  <ul>
    <li>Team Statistics</li>
    <li>Player Background</li>
    <li>Live Scores</li>
    <li>Schedules</li>
    <li>Past Team and Player Performance</li>
  </ul>
  <h3>END THE HASSLE!</h3>
  <p>Why bother visiting different websites to find live scores, player stats, schedules and past game performance. All of this is available on RUNLARK! This easy to use app puts it all at your fingertips. Simply select from the convenient drop down menus and tabs and you can research a team, it's matchups or a player by their name or jersey number.</p>
  <h3>GET THE NUMBERS!</h3>
  <p>Stats for the PFL, NCSA Division 1 College Football, PBL, PBA, PHL, and English Top League Soccer. More sports coming soon.</p>
</section>

<div class="phone"><div class="phone-screen" role="img" aria-label="App screen showing a stadium photo and team stats menu"></div></div>
<div class="store-badge" role="img" aria-label="App store download badge"></div>

<section class="features">
  <article class="feature">
    <div class="feature-shot shot-a" role="img" aria-label="Hands holding a phone with the app"></div>
    <h4>On The Go And You Need To Know!</h4>
    <p>Check live scores, schedules and player numbers anywhere with a quick tap on your phone.</p>
    <div class="free">FREE</div>
  </article>
  <article class="feature">
    <div class="feature-shot shot-b" role="img" aria-label="Night view of a packed stadium"></div>
    <h4>Have You Ever Been Watching a Game and You Want to Know More about a Team or Player Stats?</h4>
    <p>Pull up any team or player in seconds and follow every play as it happens.</p>
    <div class="free">FREE</div>
  </article>
  <article class="feature">
    <div class="feature-shot shot-c" role="img" aria-label="Laptop showing sport stats"></div>
    <h4>Perfect for the fantasy game player. Get team and player stats from previous games they played.</h4>
    <p>Compare past results and build a stronger lineup before the next kickoff arrives.</p>
    <div class="free">FREE</div>
  </article>
</section>

<footer class="footer"></footer>
</body>
</html>
```